Velmora Homecare - Website

MUST HAVE EXPERIENCE DESIGNING WEBSITES HEALTH CARE IN GENERAL AND/OR HOME NURSING SERVICES.

Details attached.

Number of Pages Required

1 page

Requirements
Must have
• Warm feel
caregivers

Color similar to the logo...

```html
<!DOCTYPE html>
<html lang="en">
<head>
<meta charset="utf-8">
<title>Velmora Homecare</title>
<link href="https://fonts.googleapis.com/css2?family=Montserrat:wght@400;500;600;700;800&family=Open+Sans:wght@400;600&display=swap" rel="stylesheet">
<style>
:root{
  --teal:#0f8b9b;
  --teal-dark:#0a6e7b;
  --orange:#f47b20;
  --ink:#2b2f33;
  --muted:#8a9096;
  --light:#f4f6f7;
  --dark:#1b2326;
  --white:#ffffff;
}
*{box-sizing:border-box;margin:0;padding:0}
html,body{width:1200px;height:3532px;overflow:hidden}
body{position:relative;background:var(--white);font-family:"Open Sans",Arial,sans-serif;color:var(--ink)}
.abs{position:absolute}
h1,h2,h3,.nav,.btn,.brand{font-family:"Montserrat",Arial,sans-serif}

/* header */
.header{top:0;left:0;width:1200px;height:88px;background:var(--white)}
.brand{left:120px;top:20px;display:flex;align-items:center;gap:12px;font-weight:800;font-size:30px;color:var(--teal)}
.brand-dot{width:40px;height:40px;border-radius:50%;background:var(--orange)}
.call{left:630px;top:30px;display:flex;align-items:center;gap:10px;font-family:"Montserrat",sans-serif;font-weight:700;font-size:20px;color:var(--ink)}
.call-icon{width:30px;height:30px;border-radius:50%;background:var(--orange);display:flex;align-items:center;justify-content:center}
.btn{display:inline-flex;align-items:center;justify-content:center;gap:8px;background:var(--orange);color:var(--white);font-weight:700;font-size:14px;border-radius:24px;letter-spacing:.5px}
.login{left:948px;top:22px;width:112px;height:42px}
.nav{top:88px;left:0;width:1200px;height:34px;background:var(--teal);display:flex;padding-left:120px;font-size:12px;font-weight:600;color:var(--white)}
.nav span{padding:0 14px;line-height:34px}
.nav span.active{background:var(--orange)}

/* hero */
.hero{top:122px;left:0;width:1200px;height:600px;background:linear-gradient(90deg,#bfdde0 0%,#d9cfc4 18%,#efe1d6 34%,#f6ece4 50%,#f3e6da 72%,#d7b7a2 100%)}
.hero-title{left:560px;top:275px;width:380px;text-align:center;font-family:"Montserrat",sans-serif;font-weight:700;font-size:62px;line-height:72px}
.hero-title .a{color:var(--ink)}
.hero-title .b{color:var(--teal)}
.get-started{left:515px;top:478px;width:170px;height:46px}
.dots{left:560px;top:605px;display:flex;gap:8px}
.dots i{width:8px;height:8px;border-radius:50%;background:#fff;opacity:.8}

/* about */
.about-photo{left:130px;top:900px;width:360px;height:360px;border-radius:50%;background:radial-gradient(circle at 40% 40%,#f4e5da,#d5b6a0)}
.about-head{left:598px;top:855px;font-family:"Montserrat",sans-serif;font-weight:700;font-size:50px;line-height:58px;color:var(--ink)}
.about-head span{color:var(--teal);display:block;font-size:46px}
.about-head span b{color:var(--orange);font-weight:700}
.about-text{left:600px;top:1000px;width:480px;font-size:14px;line-height:27px;color:var(--muted)}
.read-more{left:598px;top:1254px;width:160px;height:46px}

/* panels */
.panel{top:1410px;width:596px;height:530px;display:flex;align-items:flex-end;justify-content:center;padding-bottom:96px}
.panel h3{color:var(--white);font-weight:700;font-size:34px;line-height:46px;text-align:center}
.panel-left{left:0;background:linear-gradient(180deg,#1f9aa7,#0d7f8d)}
.panel-right{left:604px;background:linear-gradient(180deg,#f68e3c,#e0680f)}

/* nursing */
.section-head{font-family:"Montserrat",sans-serif;font-weight:700;font-size:44px;line-height:52px;color:var(--teal)}
.section-head b{color:var(--orange);font-weight:700}
.nursing-head{left:145px;top:2058px}
.nursing-text{left:145px;top:2210px;width:430px;font-size:14px;line-height:27px;color:var(--muted)}
.feature{width:146px;height:134px;background:var(--white);border:1px solid #e3e7e9;box-shadow:0 4px 14px rgba(0,0,0,.06);display:flex;flex-direction:column;align-items:center;justify-content:center;gap:10px;text-align:center;font-size:15px;line-height:19px;color:var(--ink)}

/* care */
.care-head{left:145px;top:2475px;font-family:"Montserrat",sans-serif;font-weight:700;font-size:44px;color:var(--ink)}
.care-row{left:140px;width:930px;display:flex;justify-content:space-between}
.care-item{width:160px;display:flex;flex-direction:column;align-items:center;gap:16px;font-family:"Montserrat",sans-serif;font-weight:600;font-size:17px}
.care-ring{width:140px;height:140px;border-radius:50%;border:4px solid var(--teal);display:flex;align-items:center;justify-content:center}
.care-ring div{width:112px;height:112px;border-radius:50%;border:3px solid var(--orange);display:flex;align-items:center;justify-content:center}

/* contact */
.contact{top:2800px;left:0;width:1200px;height:680px;background:var(--dark)}
.contact-head{left:0;top:3062px;width:1200px;text-align:center;font-family:"Montserrat",sans-serif;font-weight:700;font-size:48px;color:var(--teal)}
.contact-head b{color:var(--orange);font-weight:700}
.sub{font-family:"Montserrat",sans-serif;font-weight:600;font-size:17px;color:var(--white)}
.field{background:var(--white);height:28px;border-radius:2px;font-size:12px;color:#9aa0a5;padding:6px 10px}
.submit{left:525px;top:3392px;width:80px;height:28px;font-size:11px}
.info-row{display:flex;align-items:center;gap:14px;font-size:12px;line-height:18px;color:#cfd4d7}
.info-icon{width:30px;height:30px;flex:none;border-radius:50%;background:var(--white);display:flex;align-items:center;justify-content:center}
.social{display:flex;gap:8px}
.social i{width:26px;height:26px;border-radius:50%;background:#e9ecee}
.footer{top:3480px;left:0;width:1200px;height:52px;background:#141a1c;text-align:center;line-height:52px;font-size:12px;color:#c3c8cb}
</style>
</head>
<body>

<header class="abs header">
  <div class="abs brand"><span class="brand-dot"></span>Velmora Homecare</div>
  <div class="abs call">
    <span class="call-icon"><svg width="16" height="16" viewBox="0 0 24 24"><path fill="#fff" d="M6.6 10.8a15 15 0 0 0 6.6 6.6l2.2-2.2c.3-.3.7-.4 1-.2 1.1.4 2.3.6 3.6.6.6 0 1 .4 1 1V20c0 .6-.4 1-1 1A17 17 0 0 1 3 4c0-.6.4-1 1-1h3.5c.6 0 1 .4 1 1 0 1.3.2 2.5.6 3.6.1.3 0 .7-.2 1z"/></svg></span>
    CALL US : 1 800 555 0142
  </div>
  <div class="abs btn login">LOGIN</div>
</header>
<nav class="abs nav">
  <span class="active">HOME</span><span>SERVICES</span><span>CONTACT US</span><span>JOIN OUR TEAM</span><span>ABOUT US</span><span>NEWS FEED</span><span>SERVICE REQUEST</span><span>CORONAVIRUS UPDATE</span><span>TESTIMONIALS</span>
</nav>

<section class="abs hero" role="img" aria-label="Caregiver with an elderly woman on the left and a mother holding her baby on the right"></section>
<h1 class="abs hero-title"><span class="a">VELMORA</span><br><span class="b">HOMECARE</span></h1>
<div class="abs btn get-started">GET STARTED <svg width="12" height="12" viewBox="0 0 12 12"><circle cx="6" cy="6" r="5" fill="#fff"/><path d="M5 3.5 7.5 6 5 8.5" stroke="#f47b20" stroke-width="1.6" fill="none"/></svg></div>
<div class="abs dots"><i></i><i></i><i></i><i></i></div>
<svg class="abs" style="left:0;top:660px" width="1200" height="80" viewBox="0 0 1200 80">
  <path d="M0 0 C300 70 900 70 1200 0 V80 H0Z" fill="#fff"/>
</svg>

<div class="abs about-photo" role="img" aria-label="Mother smiling with her baby"></div>

<h2 class="abs about-head">ABOUT<span>VELMORA <b>HOMECARE</b></span></h2>
<p class="abs about-text">Velmora Homecare delivers compassionate care to new parents and babies, and to elderly family members in their own homes. We place the needs of our clients and their families at the heart of everything we do, offering trusted nursing support for every stage of life, from newborns to seniors. Our team is available day and night, with flexible hourly, daily, weekly and monthly packages.</p>
<div class="abs btn read-more">READ MORE <svg width="12" height="12" viewBox="0 0 12 12"><circle cx="6" cy="6" r="5" fill="#fff"/><path d="M5 3.5 7.5 6 5 8.5" stroke="#f47b20" stroke-width="1.6" fill="none"/></svg></div>

<div class="abs panel panel-left" role="img" aria-label="Nurse caring for an elderly woman at home"><h3>HOME NURSING<br>SERVICES</h3></div>
<div class="abs panel panel-right" role="img" aria-label="Newborn baby sleeping"><h3>NEW BORN BABY AND<br>MOTHER CARE AT HOME</h3></div>
<svg class="abs" style="left:258px;top:1938px" width="80" height="34" viewBox="0 0 80 34"><path d="M0 0H80L40 34Z" fill="#0d7f8d"/></svg>

<div class="abs" role="img" aria-label="Faded photo of a caregiver with an elderly person" style="left:0;top:2330px;width:1200px;height:470px;background:linear-gradient(180deg,#fff 0%,#f2f2f2 60%,#e9e9e9 100%)"></div>

<h2 class="abs section-head nursing-head">HOME <b>NURSING</b><br>SERVICES</h2>
<p class="abs nursing-text">Looking for safe, reliable care at home? Our qualified nurses provide medication support, personal care and companionship so your loved ones can stay comfortable where they belong. Every plan is built around the needs of the person we support.</p>

<div class="abs feature" style="left:745px;top:2052px">
  <svg width="40" height="36" viewBox="0 0 40 36" fill="none" stroke="#0f8b9b" stroke-width="2.4"><rect x="3" y="3" width="34" height="22" rx="2"/><path d="M8 16h6l3-6 4 10 3-4h8" stroke="#f47b20"/><path d="M14 32h12M20 25v7"/></svg>
  Monitoring<br>of medication</div>
<div class="abs feature" style="left:909px;top:2052px">
  <svg width="36" height="36" viewBox="0 0 36 36" fill="none" stroke="#0f8b9b" stroke-width="2.4"><circle cx="18" cy="9" r="5"/><path d="M7 33v-8a11 11 0 0 1 22 0v8"/><path d="M14 22h8M18 18v8" stroke="#f47b20"/></svg>
  Personal<br>Care</div>
<div class="abs feature" style="left:745px;top:2196px">
  <svg width="40" height="36" viewBox="0 0 40 36" fill="none" stroke="#0f8b9b" stroke-width="2.4"><rect x="3" y="6" width="34" height="27" rx="2"/><path d="M3 14h34M11 2v8M29 2v8"/><path d="M13 24l5 4 9-9" stroke="#f47b20"/></svg>
  Weekend and<br>holiday care</div>
<div class="abs feature" style="left:909px;top:2196px">
  <svg width="40" height="36" viewBox="0 0 40 36" fill="none" stroke="#0f8b9b" stroke-width="2.4"><rect x="3" y="3" width="34" height="24" rx="2"/><circle cx="14" cy="15" r="4" stroke="#f47b20"/><circle cx="26" cy="15" r="4" stroke="#f47b20"/><path d="M12 33h16M20 27v6"/></svg>
  Social &amp; recreational<br>activities</div>

<h2 class="abs care-head">Care Offered</h2>
<div class="abs care-row" style="top:2555px">
  <div class="care-item"><div class="care-ring"><div><svg width="44" height="52" viewBox="0 0 44 52" fill="none" stroke="#0f8b9b" stroke-width="3"><path d="M22 4c-8 0-10 10-4 20L6 48M22 4c8 0 10 10 4 20l12 24"/></svg></div></div>Cancer Care</div>
  <div class="care-item"><div class="care-ring"><div><svg width="52" height="44" viewBox="0 0 52 44" fill="none" stroke="#0f8b9b" stroke-width="3"><circle cx="16" cy="10" r="6"/><circle cx="36" cy="10" r="6"/><path d="M4 42V30a12 12 0 0 1 24 0M24 42V30a12 12 0 0 1 24 0v12"/></svg></div></div>Companionship</div>
  <div class="care-item"><div class="care-ring"><div><svg width="48" height="48" viewBox="0 0 48 48" fill="none" stroke="#0f8b9b" stroke-width="3"><path d="M30 44v-8h6v-10l4-2-4-8A16 16 0 1 0 12 36v8"/><path d="M20 18h8M24 14v8" stroke="#f47b20"/></svg></div></div>Dementia</div>
  <div class="care-item"><div class="care-ring"><div><svg width="44" height="52" viewBox="0 0 44 52" fill="none" stroke="#0f8b9b" stroke-width="3"><circle cx="18" cy="8" r="5"/><path d="M18 14v16l-6 18M18 30l8 18M10 22h14"/><path d="M32 20v28" stroke="#f47b20"/></svg></div></div>Elderly Care</div>
  <div class="care-item"><div class="care-ring"><div><svg width="50" height="46" viewBox="0 0 50 46" fill="none" stroke="#0f8b9b" stroke-width="3"><path d="M25 40S6 28 6 15a9 9 0 0 1 19-4 9 9 0 0 1 19 4c0 13-19 25-19 25z"/><path d="M19 20h12M25 14v12" stroke="#f47b20"/></svg></div></div>Palliative Care</div>
</div>
<svg class="abs" style="left:96px;top:2616px" width="16" height="26" viewBox="0 0 16 26"><path d="M14 2 3 13l11 11" stroke="#b9bec2" stroke-width="3" fill="none"/></svg>
<svg class="abs" style="left:1092px;top:2616px" width="16" height="26" viewBox="0 0 16 26"><path d="M2 2l11 11L2 24" stroke="#b9bec2" stroke-width="3" fill="none"/></svg>

<section class="abs contact"></section>
<svg class="abs" style="left:0;top:2800px" width="1200" height="160" viewBox="0 0 1200 160">
  <path d="M0 0H1200V20C900 120 300 120 0 20Z" fill="#ececec"/>
  <path d="M0 20C300 120 900 120 1200 20" stroke="#0f8b9b" stroke-width="3" fill="none"/>
</svg>
<h2 class="abs contact-head">CONTACT <b>US</b></h2>

<div class="abs sub" style="left:145px;top:3160px">Get in Touch</div>
<div class="abs field" style="left:145px;top:3200px;width:225px">Name</div>
<div class="abs field" style="left:380px;top:3200px;width:225px">Phone</div>
<div class="abs field" style="left:145px;top:3238px;width:460px">Email</div>
<div class="abs field" style="left:145px;top:3276px;width:460px;height:100px">Message</div>
<div class="abs btn submit">SUBMIT</div>

<div class="abs sub" style="left:760px;top:3160px">Contact Information</div>
<div class="abs" style="left:760px;top:3200px;display:flex;flex-direction:column;gap:18px">
  <div class="info-row"><span class="info-icon"><svg width="14" height="16" viewBox="0 0 14 16"><path d="M7 1a5 5 0 0 0-5 5c0 4 5 9 5 9s5-5 5-9a5 5 0 0 0-5-5z" fill="#1b2326"/><circle cx="7" cy="6" r="2" fill="#fff"/></svg></span>245 Cedar Bend Road, Suite 12,<br>Tempe</div>
  <div class="info-row"><span class="info-icon"><svg width="14" height="14" viewBox="0 0 24 24"><path fill="#1b2326" d="M6.6 10.8a15 15 0 0 0 6.6 6.6l2.2-2.2c.3-.3.7-.4 1-.2 1.1.4 2.3.6 3.6.6.6 0 1 .4 1 1V20c0 .6-.4 1-1 1A17 17 0 0 1 3 4c0-.6.4-1 1-1h3.5c.6 0 1 .4 1 1 0 1.3.2 2.5.6 3.6.1.3 0 .7-.2 1z"/></svg></span>Phone : 1 800 555 0142</div>
  <div class="info-row"><span class="info-icon"><svg width="16" height="12" viewBox="0 0 16 12"><rect x="1" y="1" width="14" height="10" fill="none" stroke="#1b2326" stroke-width="1.6"/><path d="M1 1l7 6 7-6" fill="none" stroke="#1b2326" stroke-width="1.6"/></svg></span>Email : info@velmorahomecare.com</div>
  <div class="social"><i></i><i></i><i></i><i></i><i></i></div>
</div>

<footer class="abs footer">Copyright © 2021, Velmora Homecare. All Rights Reserved. | Privacy policy</footer>

</body>
</html>
```